Inspiration Poster

Inspirational Poster that has a Kamran Dulo like abstract look (http://www.vexalo.com/images/search?q=kamran+dulo&FORM=HDRSC2) with the text:

"we walk not in order to arrive at the promise land but because walking itself is a revolution"
-Peter Ambrick

```html
<!DOCTYPE html>
<html lang="en">
<head>
<meta charset="utf-8">
<title>We Walk — Inspiration Poster</title>
<link rel="stylesheet" href="https://fonts.googleapis.com/css2?family=Josefin+Sans:wght@700&family=Roboto+Condensed:wght@500&display=swap">
<style>
  :root {
    --ink-night: #04060b;
    --deep-blue: #14264a;
    --sky-blue: #3d64b0;
    --frost: #b9c8dc;
    --rust: #b2401a;
    --amber: #f3a51e;
    --sun-yellow: #fcc93a;
    --ember: #e8660f;
    --headline: #ffffff;
    --accent: #f7ee2a;
  }
  * { margin: 0; padding: 0; box-sizing: border-box; }
  html, body {
    width: 849px;
    height: 1200px;
    overflow: hidden;
    background: var(--ink-night);
  }
  .poster {
    position: relative;
    width: 849px;
    height: 1200px;
    overflow: hidden;
  }
  .artwork {
    position: absolute;
    inset: 0;
    background:
      radial-gradient(ellipse 260px 200px at 90px 250px, rgba(185,200,220,0.75), transparent 70%),
      radial-gradient(ellipse 300px 160px at 240px 380px, rgba(61,100,176,0.7), transparent 75%),
      radial-gradient(ellipse 320px 120px at 700px 560px, rgba(60,20,10,0.8), transparent 70%),
      radial-gradient(ellipse 340px 240px at 480px 690px, rgba(255,236,150,0.55), transparent 70%),
      linear-gradient(180deg,
        var(--ink-night) 0%,
        #0a1220 12%,
        var(--deep-blue) 28%,
        var(--sky-blue) 38%,
        var(--rust) 46%,
        #d8781c 52%,
        var(--amber) 58%,
        var(--sun-yellow) 70%,
        var(--amber) 86%,
        var(--ember) 100%);
  }
  .quote {
    position: absolute;
    top: 30px;
    right: 34px;
    text-align: right;
    font-family: "Josefin Sans", sans-serif;
    font-weight: 700;
    font-size: 33px;
    line-height: 40px;
    letter-spacing: 0.5px;
    color: var(--headline);
    text-transform: uppercase;
  }
  .quote .line { display: block; }
  .quote .highlight { color: var(--accent); }
  .attribution {
    position: absolute;
    top: 314px;
    right: 34px;
    font-family: "Roboto Condensed", sans-serif;
    font-weight: 500;
    font-size: 15px;
    letter-spacing: 0.3px;
    color: var(--headline);
    text-transform: uppercase;
  }
</style>
</head>
<body>
  <main class="poster">
    <div class="artwork" role="img" aria-label="Abstract painted scene of a lone figure walking along a glowing golden path beneath a dark blue sky"></div>
    <blockquote class="quote">
      <span class="line">We <span class="highlight">walk</span></span>
      <span class="line">not in order</span>
      <span class="line">to arrive at</span>
      <span class="line">the promise land</span>
      <span class="line">but because</span>
      <span class="line">walking itself</span>
      <span class="line">is a <span class="highlight">revolution</span></span>
    </blockquote>
    <p class="attribution">- Peter Ambrick</p>
  </main>
</body>
</html>
```